Radon Reduction & Mold Removal Website

I need you to set up a WordPress account for me and design a full width, professional-looking, mobile-responsive website for my business. We offer radon reduction and mold removal (two household environmental issues).
We have merged 2 companies and need a single website to promote both services (radon and mold). Here are the current websites from the 2 businesses that have merged:
RADON
http://klendor-airfix.com/
MOLD
http://brisketfungusclear.net/
Once complete, I will need the login to the WordPress account so I have access to the site to make changes, additions, and modifications.
Target Market(s)
Home Owners
Industry/Entity Type
Home And Garden
Look and feel
Each slider illustrates characteristics of the customer's brand and the style your logo design should communicate.

```html
<!DOCTYPE html>
<html lang="en">
<head>
<meta charset="utf-8">
<title>Klendor Airfix – Radon Mitigation &amp; Mold Removal</title>
<link href="https://fonts.googleapis.com/css2?family=Open+Sans:wght@400;600;700&family=Oswald:wght@500;700&display=swap" rel="stylesheet">
<style>
:root{
  --green:#6cbf1c;
  --green-dark:#3f9a12;
  --green-light:#8fd43a;
  --ink:#222;
  --muted:#666;
  --darker:#111;
  --yellow:#ece21c;
  --white:#fff;
  --grey:#eeeeee;
}
*{box-sizing:border-box;margin:0;padding:0}
html,body{width:1200px;height:2564px;overflow:hidden}
body{font-family:"Open Sans",Arial,sans-serif;color:var(--ink);background:var(--white);position:relative}
.abs{position:absolute}
.btn-quote{display:inline-block;background:var(--yellow);color:#222;font-weight:700;font-size:16px;padding:9px 20px;border-radius:22px;box-shadow:0 2px 4px rgba(0,0,0,.4)}
.btn-more{display:inline-block;border:2px solid var(--green);color:#333;font-size:13px;font-weight:600;padding:3px 26px;border-radius:16px;background:#fff}

/* hero */
.hero{left:0;top:0;width:1200px;height:744px;background:linear-gradient(100deg,#5a4a3c 0%,#7b6d5f 25%,#3a3836 45%,#6e6e6c 70%,#b6b6b2 100%)}
.hero-shade{left:0;top:0;width:1200px;height:744px;background:linear-gradient(180deg,rgba(0,0,0,.55) 0%,rgba(0,0,0,.2) 30%,rgba(0,0,0,.3) 100%)}
.brand{left:115px;top:14px;height:80px;display:flex;align-items:center;gap:12px}
.brand-mark{width:28px;height:28px;background:var(--yellow)}
.brand-name{font-size:32px;font-weight:700;color:var(--yellow);letter-spacing:1px}
.top-phone{right:100px;top:14px;color:#fff;font-size:18px}
.top-phone b{color:var(--yellow)}
.nav{left:590px;top:64px;display:flex;gap:18px;align-items:center}
.nav a{color:#fff;font-size:13px;font-weight:600;text-decoration:none;padding:6px 16px}
.nav a.active{border:2px solid var(--green);border-radius:18px}
.hero-caption{left:174px;top:246px;width:513px;height:195px;background:rgba(0,0,0,.7);padding:18px 14px}
.hero-caption h1{font-size:28px;font-weight:600;color:var(--green-light);margin-bottom:8px}
.hero-caption p{color:#ddd;font-size:13px;line-height:1.55;margin-bottom:12px}
.arrow{top:296px}

/* intro panel */
.intro{left:115px;top:526px;width:970px;height:205px;background:#fff;border-radius:6px;box-shadow:0 2px 10px rgba(0,0,0,.25);text-align:center;padding:22px 50px}
.intro h2{font-size:34px;font-weight:400;margin-bottom:14px}
.intro h2 span{color:var(--green)}
.intro p{font-size:12.5px;line-height:1.65;color:var(--muted);margin-bottom:10px}

/* fix band */
.fix{left:0;top:744px;width:1200px;height:115px;background:var(--darker)}
.fix-tag{left:0;top:744px;width:300px;height:115px;background:var(--green);clip-path:polygon(0 0,88% 0,100% 50%,88% 100%,0 100%)}
.fix-tag p{font-family:Oswald,sans-serif;color:#fff;font-size:30px;font-weight:700;line-height:1.2;padding:20px 0 0 110px}
.fix-text{left:320px;top:762px;width:580px;color:#fff;font-size:17px;line-height:1.5}
.fix-phone{left:905px;top:780px;color:var(--yellow);font-family:Oswald,sans-serif;font-size:30px;display:flex;align-items:center;gap:10px}

/* services */
.services{left:0;top:859px;width:1200px;height:167px;background:var(--grey)}
.svc{top:890px;display:flex;gap:16px;width:330px}
.svc-icon{width:86px;height:86px;border-radius:50%;background:#fff;box-shadow:0 2px 5px rgba(0,0,0,.2);display:flex;align-items:center;justify-content:center;flex:none}
.svc h3{font-size:20px;font-weight:600;color:var(--green);line-height:1.15;margin-top:2px}
.svc h3 span{color:#333}
.svc p{font-size:12.5px;color:var(--muted);margin-top:6px;line-height:1.4}

/* video */
.video{left:115px;top:1064px;width:540px;height:290px;background:linear-gradient(135deg,#3b342c,#8a7a66 50%,#2a2622)}
.video-bar{left:115px;top:1326px;width:540px;height:28px;background:#000}
.story{left:675px;top:1056px;width:420px}
.story h2{font-size:30px;font-weight:400;color:var(--green);line-height:1.2;margin-bottom:14px}
.story p{font-size:12.5px;color:var(--muted);line-height:1.55;margin-bottom:10px}

/* what is radon */
.what{left:0;top:1397px;width:1200px;height:321px;background:linear-gradient(180deg,var(--green-dark),var(--green));text-align:center;padding:38px 110px}
.what h2{color:#fff;font-size:34px;font-weight:400;margin-bottom:14px}
.what p{color:#eef;font-size:12.5px;line-height:1.6;margin-bottom:20px}

/* gallery */
.gallery-title{left:0;top:1752px;width:1200px;text-align:center;font-size:34px;font-weight:400}
.gallery-title span{color:var(--green)}
.photo{top:1826px;height:161px;border:6px solid #fff;box-shadow:0 1px 6px rgba(0,0,0,.3)}

/* about */
.about{left:0;top:2033px;width:1200px;height:287px;background:linear-gradient(180deg,var(--green-dark),var(--green) 60%,var(--green-dark))}
.about-text{left:115px;top:2056px;width:970px;color:#fff;font-size:12.5px;line-height:1.6;text-align:center}
.badge{top:2169px;height:103px;background:#fff;border-radius:4px;box-shadow:0 2px 5px rgba(0,0,0,.3);display:flex;align-items:center;justify-content:center}

/* footer */
.footer{left:0;top:2320px;width:1200px;height:213px;background:#2a2a2a}
.fcol{top:2342px;color:#bbb;font-size:12.5px;line-height:1.6}
.fcol h4{color:#fff;font-size:19px;font-weight:400;margin-bottom:12px}
.fcol .hl{color:var(--green-light)}
.input{width:240px;height:30px;background:#fff;color:#999;font-size:11px;padding:6px 8px;margin:4px 0 10px}
.btn-sign{display:inline-block;background:var(--yellow);color:#222;font-weight:700;font-size:15px;padding:4px 14px}
.row{display:flex;align-items:center;gap:8px}
.bottom{left:0;top:2533px;width:1200px;height:31px;background:#141414;color:#999;font-size:11px}
.bottom .links{left:115px;top:8px;display:flex;gap:22px}
.bottom .copy{right:115px;top:8px}
</style>
</head>
<body>

<div class="abs hero" role="img" aria-label="Townhouse exterior with a radon mitigation fan mounted on the pipe"></div>
<div class="abs hero-shade"></div>

<div class="abs brand"><span class="brand-mark"></span><span class="brand-name">Klendor Airfix</span></div>
<div class="abs top-phone">Radon &amp; Mold : <b>1-800-555-0142</b></div>
<nav class="abs nav">
  <a class="active">HOME</a><a>SERVICES</a><a>CONTACT</a><a>PRODUCTS</a><a>GET A QUOTE</a>
</nav>

<svg class="abs arrow" style="left:110px" width="30" height="70" viewBox="0 0 30 70"><path d="M26 4 4 35 26 66" fill="none" stroke="rgba(255,255,255,.7)" stroke-width="3"/></svg>
<svg class="abs arrow" style="left:1060px" width="30" height="70" viewBox="0 0 30 70"><path d="M4 4 26 35 4 66" fill="none" stroke="rgba(255,255,255,.7)" stroke-width="3"/></svg>

<div class="abs hero-caption">
  <h1>PROTECT WHAT'S IMPORTANT</h1>
  <p>Klendor Airfix is the best choice for radon mitigation and mold removal for your home or business. Radon is the number one cause of lung cancer among non-smokers, and hidden mold can harm your family's health.</p>
  <span class="btn-quote">GET A QUOTE !</span>
</div>

<section class="abs intro">
  <h2>Radon Mitigation and <span>Mold Removal</span></h2>
  <p>High levels of radon have been found in every state across America, and mold grows wherever moisture is left unchecked. Radon mitigation, radon testing and mold remediation have become more prevalent in residential, commercial and real-estate environments, with state and local regulations now mandating testing before homes go on the market.</p>
  <span class="btn-more">More</span>
</section>

<div class="abs fix"></div>
<div class="abs fix-tag"><p>FIX YOUR<br>HOME TODAY</p></div>
<p class="abs fix-text">Radon mitigation and mold removal company helping resolve your indoor air issues. We reduce radon levels and clear mold from your home so you will be safe.</p>
<div class="abs fix-phone">
  <svg width="22" height="26" viewBox="0 0 22 26"><path d="M5 1 9 7 6 10c1 4 4 8 8 10l3-3 5 4-3 4C9 24 2 15 1 4z" fill="var(--yellow)"/></svg>
  1-800-555-0142
</div>

<div class="abs services"></div>
<div class="abs svc" style="left:115px">
  <div class="svc-icon"><svg width="44" height="40" viewBox="0 0 44 40"><path d="M22 3 2 20h6v17h11V27h6v10h11V20h6z" fill="#333"/></svg></div>
  <div><h3>RESIDENTIAL<br><span>SERVICES</span></h3><p>Certified radon and mold technicians for every home.</p></div>
</div>
<div class="abs svc" style="left:445px">
  <div class="svc-icon"><svg width="40" height="42" viewBox="0 0 40 42"><rect x="8" y="4" width="24" height="36" fill="#333"/><g fill="#fff"><rect x="12" y="9" width="5" height="5"/><rect x="23" y="9" width="5" height="5"/><rect x="12" y="18" width="5" height="5"/><rect x="23" y="18" width="5" height="5"/><rect x="17" y="30" width="6" height="10"/></g></svg></div>
  <div><h3>COMMERCIAL<br><span>SERVICES</span></h3><p>Radon and mold solutions for offices and buildings.</p></div>
</div>
<div class="abs svc" style="left:775px">
  <div class="svc-icon"><svg width="42" height="42" viewBox="0 0 42 42"><path d="M21 4 4 18h5v18h24V18h5z" fill="none" stroke="#333" stroke-width="3"/><text x="21" y="31" font-size="14" font-weight="700" text-anchor="middle" fill="#333" font-family="Open Sans,sans-serif">$</text></svg></div>
  <div><h3>REAL ESTATE<br><span>SERVICES</span></h3><p>Fast radon tests and mold checks for home sales.</p></div>
</div>

<div class="abs video" role="img" aria-label="Video still of a technician fitting a white radon vent pipe"></div>
<svg class="abs" style="left:352px;top:1170px" width="66" height="66" viewBox="0 0 66 66"><circle cx="33" cy="33" r="31" fill="rgba(0,0,0,.5)" stroke="rgba(255,255,255,.6)" stroke-width="2"/><path d="M26 20v26l20-13z" fill="#fff"/></svg>
<div class="abs video-bar"></div>
<svg class="abs" style="left:125px;top:1331px" width="520" height="18" viewBox="0 0 520 18"><path d="M4 3v12l10-6z" fill="#ddd"/><rect x="26" y="8" width="330" height="3" fill="#555"/><text x="370" y="13" font-size="10" fill="#ccc" font-family="Open Sans,sans-serif">00:00:00</text><rect x="440" y="5" width="10" height="8" fill="#ccc"/><rect x="470" y="8" width="30" height="3" fill="#888"/></svg>

<article class="abs story">
  <h2>Nonsmoking woman believes radon caused her lung cancer</h2>
  <p>BELLVILLE, OH (WKLX) - It is the number one cause of lung cancer in nonsmokers and it could be in your house. One woman believes radon in her home made her sick.</p>
  <p>Warning about radon levels in homes One thing becomes quickly clear when a radon reduction system is being installed, everything must be tightly sealed for it to work properly, according to removal expert Gil Parrow. He installed a system in Nora and Ted Lindqvist's home.</p>
  <span class="btn-more">More</span>
</article>

<section class="abs what">
  <h2>What is Radon?</h2>
  <p>Radon is everywhere indoor and outdoor with the highest levels being found indoor where radon is more concentrated and takes longer to break down. Radon is a radioactive gas that is caused by the decay of uranium in the soil. Radon gas is a colorless, odorless, and invisible gas that can only be detected by radon testing. Radon can penetrate most common building materials and is fairly soluble in water. Exposure to radon is most common through ingestion and inhalation, with inhalation being the largest threat to your health. Radon Awareness has grown exponentially over the past 10 years and is only becoming a more common issue nationwide. Radon Gas and Radon awareness are imperative to the health and future of you and your loved ones. Visit our Radon and Mold Information pages to learn more about the dangers of radon gas and mold, and what you can do to keep everyone safe.</p>
  <span class="btn-quote">GET A QUOTE !</span>
</section>

<h2 class="abs gallery-title">Photo <span>Gallery</span></h2>
<svg class="abs" style="left:108px;top:1870px" width="22" height="60" viewBox="0 0 22 60"><path d="M19 3 3 30l16 27" fill="none" stroke="#ccc" stroke-width="3"/></svg>
<svg class="abs" style="left:1068px;top:1870px" width="22" height="60" viewBox="0 0 22 60"><path d="M3 3l16 27L3 57" fill="none" stroke="#ccc" stroke-width="3"/></svg>
<div class="abs photo" style="left:154px;width:200px;background:linear-gradient(160deg,#8fb3d6,#6b7b8c 55%,#d8d2c6)" role="img" aria-label="House exterior with a radon vent pipe"></div>
<div class="abs photo" style="left:385px;width:197px;background:linear-gradient(150deg,#c7704a,#e0a27e 50%,#8a4a2c)" role="img" aria-label="Copper pipes and fittings in a basement"></div>
<div class="abs photo" style="left:615px;width:200px;background:linear-gradient(160deg,#9a9a96,#e8e8e4 45%,#4c4c48)" role="img" aria-label="White radon fan and sump cover on a basement floor"></div>
<div class="abs photo" style="left:851px;width:200px;background:linear-gradient(160deg,#6fa0d6,#c9b79a 55%,#8a7a66)" role="img" aria-label="Tall home exterior with vent pipe under blue sky"></div>

<div class="abs about"></div>
<p class="abs about-text">Klendor Airfix is quickly becoming a household name across the United States. Offering radon reduction and mold removal in over forty locations across America has made us the golden standard for healthy indoor air. We were not always such a large company, and actually started from very humble beginnings. We began in 1988 with only one radon specialist. Now we boast a team of over 100 employees, and have experienced tremendous growth over the past ten years! As we continue to grow we strive to keep our quality of work to the same standard.</p>
<div class="abs badge" style="left:120px;width:129px"><svg width="90" height="60"><rect x="5" y="10" width="80" height="40" fill="#c33"/></svg></div>
<div class="abs badge" style="left:300px;width:126px"><svg width="90" height="60"><circle cx="45" cy="30" r="25" fill="#e6a020"/></svg></div>
<div class="abs badge" style="left:469px;width:128px"><svg width="80" height="80"><circle cx="40" cy="40" r="34" fill="none" stroke="#888" stroke-width="4"/></svg></div>
<div class="abs badge" style="left:641px;width:169px"><svg width="130" height="60"><rect x="5" y="8" width="120" height="44" rx="6" fill="none" stroke="#c22" stroke-width="3"/></svg></div>
<div class="abs badge" style="left:856px;width:223px"><svg width="180" height="70"><rect x="5" y="8" width="170" height="54" rx="8" fill="var(--green-light)"/></svg></div>

<div class="abs footer"></div>
<div class="abs fcol" style="left:115px;width:230px">
  <h4>Client Testimonial</h4>
  <p class="hl">.... Out Standing ...</p>
  <p>Klendor Airfix is quickly becoming a household name across the United States. Offering radon ...</p>
  <p class="hl">Marla T</p>
</div>
<div class="abs fcol" style="left:378px;width:260px">
  <h4>Newsletter Signup</h4>
  <p>Mail id :</p>
  <div class="input">Enter your email id here</div>
  <span class="btn-sign">Sign up</span>
</div>
<div class="abs fcol" style="left:655px;width:230px">
  <h4>Contact Us</h4>
  <p style="color:#ddd;font-weight:600">Corporate Headquarters</p>
  <p class="row"><svg width="12" height="12" viewBox="0 0 22 26"><path d="M5 1 9 7 6 10c1 4 4 8 8 10l3-3 5 4-3 4C9 24 2 15 1 4z" fill="#bbb"/></svg>1-800-555-0142</p>
  <p class="row"><svg width="13" height="10" viewBox="0 0 13 10"><rect x=".5" y=".5" width="12" height="9" fill="none" stroke="#bbb"/><path d="M.5.5 6.5 6l6-5.5" fill="none" stroke="#bbb"/></svg>hello@klendorairfix.com</p>
</div>
<div class="abs fcol" style="left:890px;width:200px">
  <h4>Opening hours</h4>
  <p>◦ Mon - Fri : 7am - 8pm</p>
  <p>◦ Sat : 8am - 3pm</p>
</div>

<div class="abs bottom">
  <div class="abs links"><span>Terms of Use</span><span>Privacy Policy</span><span>Directory</span></div>
  <div class="abs copy">Copyright © 2015 Radon Mitigation &amp; Mold Removal | Klendor Airfix Environmental Services</div>
</div>

</body>
</html>
```